KVRo Business Cards

We need a business card design. We are a Technology (Audio Visual) design, sales and installation company. Looking for a double sided design, clean

Contact Information for Business Card

Clean, modern look, 2 sided

Font styles to use
Sans Serif

```html
<!DOCTYPE html>
<html lang="en">
<head>
<meta charset="utf-8">
<title>KVRo Business Cards</title>
<link rel="stylesheet" href="https://fonts.googleapis.com/css2?family=Lato:wght@400;700;900&display=swap">
<style>
  :root {
    --navy: #1b3041;
    --orange: #f59a23;
    --white: #ffffff;
    --backdrop: #d3d3ce;
  }
  * { box-sizing: border-box; margin: 0; padding: 0; }
  html, body {
    width: 1200px; height: 801px; overflow: hidden;
    background: var(--backdrop);
    font-family: "Lato", Arial, sans-serif;
  }
  .sheet {
    width: 1200px; height: 801px;
    display: flex; align-items: center; justify-content: center; gap: 40px;
  }
  .card {
    position: relative;
    width: 540px; height: 309px;
    background: var(--navy);
    overflow: hidden;
    box-shadow: 0 10px 24px rgba(0,0,0,0.18);
  }
  .card-wave { position: absolute; inset: 0; width: 100%; height: 100%; }
  .brand {
    position: absolute;
    font-family: "Lato", Arial, sans-serif;
    font-weight: 900;
    color: var(--white);
    letter-spacing: -1px;
    line-height: 1;
  }
  .front .brand { left: 34px; top: 112px; font-size: 78px; }
  .divider {
    position: absolute; left: 248px; top: 58px;
    width: 1.5px; height: 132px; background: var(--orange);
  }
  .details {
    position: absolute; left: 266px; top: 46px;
    color: var(--white); font-size: 11px; line-height: 1.35;
  }
  .details .name {
    color: var(--orange); font-weight: 900; font-size: 19px;
    text-transform: uppercase; letter-spacing: 0.3px; line-height: 1.1;
  }
  .details .role { font-size: 12px; margin-bottom: 7px; }
  .details .address { margin-bottom: 7px; }
  .contact { display: flex; align-items: center; gap: 7px; }
  .contact svg { width: 10px; height: 10px; flex: none; }
  .back .brand { left: 330px; top: 188px; font-size: 38px; }
</style>
</head>
<body>
<main class="sheet">
  <section class="card front" aria-label="Front of card">
    <svg class="card-wave" viewBox="0 0 540 309" preserveAspectRatio="none" aria-hidden="true">
      <path d="M150 300 C 330 290, 410 255, 445 190 C 478 122, 505 74, 540 60 L540 72 C 512 86, 488 128, 457 196 C 420 268, 330 298, 150 300 Z" fill="var(--white)"/>
      <path d="M0 309 L0 298 C 210 294, 400 285, 455 215 C 490 155, 510 106, 540 88 L540 309 Z" fill="var(--orange)"/>
    </svg>
    <div class="brand">KVRo</div>
    <div class="divider"></div>
    <div class="details">
      <p class="name">John Smith</p>
      <p class="role">Founder &amp; CEO</p>
      <p class="address">1234 First Line Address<br>5678 Second Line Address</p>
      <p class="contact">
        <svg viewBox="0 0 12 12"><path d="M2.5 1 L4.5 1 L5 4 L3.8 4.8 C4.5 6.3 5.7 7.5 7.2 8.2 L8 7 L11 7.5 L11 9.5 C11 10.3 10.3 11 9.5 11 C5 11 1 7 1 2.5 C1 1.7 1.7 1 2.5 1Z" fill="var(--orange)"/></svg>
        1234567890
      </p>
      <p class="contact">
        <svg viewBox="0 0 12 12"><rect x="0.5" y="2" width="11" height="8" fill="var(--orange)"/><path d="M0.5 2 L6 6.5 L11.5 2" stroke="var(--navy)" stroke-width="1" fill="none"/></svg>
        info@yourmail.com
      </p>
      <p class="contact">
        <svg viewBox="0 0 12 12"><circle cx="6" cy="6" r="5.5" fill="var(--orange)"/><path d="M0.8 6 H11.2 M6 0.5 V11.5 M2 3.5 H10 M2 8.5 H10" stroke="var(--navy)" stroke-width="0.8"/></svg>
        www.yourwebsite.com
      </p>
    </div>
  </section>

  <section class="card back" aria-label="Back of card">
    <div class="brand">KVRo</div>
  </section>
</main>
</body>
</html>
```